Cleaning Company Banner

Looking to have a Banner made that shows our contact information and shows what we do with good imagery to catch cars driving by. Will be a 6' x 3' banner (landscape). Attached our logo and flyer that we currently hand out.

```html
<!DOCTYPE html>
<html lang="en">
<head>
<meta charset="utf-8">
<title>BrightWay Cleaning Banner</title>
<link href="https://fonts.googleapis.com/css2?family=Poppins:ital,wght@0,400;0,600;0,700;0,800;1,500&display=swap" rel="stylesheet">
<style>
  :root{
    --navy:#0f4a7c;
    --teal:#13a596;
    --panel-blue:#0b5698;
    --panel-blue-deep:#0a467f;
    --gold:#e1b71f;
    --gold-deep:#c99a12;
    --paper:#eceef1;
    --ink:#141414;
    --white:#ffffff;
    --stage:#e4e6e9;
  }
  html,body{margin:0;padding:0;width:1200px;height:1117px;overflow:hidden;background:var(--stage);}
  .stage{position:relative;width:1200px;height:1117px;}
  .banner{
    position:absolute;left:20px;top:260px;width:1635px;height:840px;
    transform:scale(0.7095);transform-origin:0 0;
    background:var(--paper);overflow:hidden;
    font-family:"Poppins",sans-serif;
    box-shadow:0 10px 30px rgba(0,0,0,.18);
  }
  .banner-art{position:absolute;inset:0;}
  .headline{
    position:absolute;left:87px;top:40px;margin:0;
    font-weight:800;font-size:62px;line-height:62px;letter-spacing:.5px;
    color:var(--navy);text-transform:uppercase;
  }
  .headline .accent{color:var(--teal);}
  .services-title{
    position:absolute;left:85px;top:490px;margin:0;
    font-weight:700;font-size:54px;color:var(--white);
  }
  .services-title span{color:var(--gold);}
  .service{
    position:absolute;display:flex;align-items:center;gap:22px;
    color:var(--white);font-size:33px;line-height:35px;font-weight:400;
  }
  .service-icon{
    width:80px;height:80px;border-radius:50%;
    border:3px solid var(--white);box-sizing:border-box;
    display:flex;align-items:center;justify-content:center;
    background:rgba(255,255,255,.06);flex:none;
  }
  .service-icon svg{width:44px;height:44px;fill:none;stroke:var(--white);stroke-width:2;stroke-linecap:round;stroke-linejoin:round;}
  .brand-name{
    position:absolute;left:860px;top:655px;width:270px;text-align:center;
    font-weight:600;font-size:40px;line-height:44px;color:var(--teal);
  }
  .contact{position:absolute;left:1160px;top:610px;}
  .contact-name{margin:0;font-weight:700;font-size:47px;line-height:52px;color:var(--panel-blue);}
  .contact-role{margin:0 0 8px;font-style:italic;font-weight:500;font-size:28px;line-height:32px;color:var(--teal);}
  .contact-line{margin:0;font-weight:600;font-size:27px;line-height:42px;color:var(--ink);}
</style>
</head>
<body>
<div class="stage">
  <section class="banner">
    <svg class="banner-art" viewBox="0 0 1635 840" width="1635" height="840">
      <defs>
        <linearGradient id="room" x1="0" y1="0" x2="1" y2="1">
          <stop offset="0" stop-color="#d8c6ad"/>
          <stop offset=".5" stop-color="#cdb9a0"/>
          <stop offset="1" stop-color="#b9a58d"/>
        </linearGradient>
        <linearGradient id="crew" x1="0" y1="0" x2="1" y2="1">
          <stop offset="0" stop-color="#2a3a5c"/>
          <stop offset=".6" stop-color="#6f6a4a"/>
          <stop offset="1" stop-color="#c49b3e"/>
        </linearGradient>
        <linearGradient id="spray" x1="0" y1="0" x2="1" y2="1">
          <stop offset="0" stop-color="#7ea06a"/>
          <stop offset=".5" stop-color="#d8b55a"/>
          <stop offset="1" stop-color="#8a5a2c"/>
        </linearGradient>
        <linearGradient id="panel" x1="0" y1="0" x2="1" y2="1">
          <stop offset="0" stop-color="var(--panel-blue)"/>
          <stop offset="1" stop-color="var(--panel-blue-deep)"/>
        </linearGradient>
        <linearGradient id="goldband" x1="0" y1="0" x2="1" y2="0">
          <stop offset="0" stop-color="var(--gold-deep)"/>
          <stop offset=".6" stop-color="var(--gold)"/>
          <stop offset="1" stop-color="#efcf4a"/>
        </linearGradient>
      </defs>

      <path role="img" aria-label="Photo of cleaning supplies in a red bucket beside a mop in a bright living room"
            fill="url(#room)"
            d="M690 0 H1635 V350 C1450 430 1250 470 1000 460 C900 456 800 450 740 440 C720 300 700 120 690 0 Z"/>

      <path fill="url(#goldband)" d="M0 445 C200 395 420 390 520 410 C640 432 760 440 900 452 C1150 470 1400 420 1635 345 V420 C1400 520 1200 560 1020 560 C850 558 700 470 560 440 C420 412 200 420 0 470 Z"/>
      <path fill="var(--panel-blue)" d="M1240 577 C1400 560 1520 520 1635 468 V485 C1520 530 1400 568 1240 580 Z"/>

      <path fill="url(#panel)" d="M0 490 C300 455 600 470 830 520 C810 620 790 740 770 840 H0 Z"/>

      <circle cx="892" cy="235" r="200" fill="var(--white)"/>
      <circle role="img" aria-label="Photo of a cleaner in yellow gloves holding a caddy of cleaning products" cx="892" cy="235" r="188" fill="url(#crew)"/>

      <circle cx="620" cy="435" r="128" fill="var(--white)"/>
      <circle role="img" aria-label="Photo of a hand spraying cleaner onto a yellow cloth" cx="620" cy="435" r="118" fill="url(#spray)"/>
    </svg>

    <h1 class="headline">Quality driven<br>and reliable to<br>take care of all<br><span class="accent">your cleaning<br>needs!!!</span></h1>

    <h2 class="services-title">Our <span>Services</span></h2>

    <div class="service" style="left:88px;top:585px;">
      <div class="service-icon"><svg viewBox="0 0 44 44"><path d="M8 20h14l-2 18H10z"/><path d="M26 16h6v22h-6z"/><path d="M28 16v-5h3l3 2"/><circle cx="36" cy="32" r="4"/></svg></div>
      <div>Residential<br>Cleaning</div>
    </div>
    <div class="service" style="left:418px;top:585px;">
      <div class="service-icon"><svg viewBox="0 0 44 44"><path d="M10 10h14l4 5h-9"/><path d="M14 10v6l-4 8v14h14V24l-4-8"/><path d="M17 28v6M14 31h6"/><path d="M32 10l2-2M34 15h3M32 20l2 2"/></svg></div>
      <div>Antiviral<br>Disinfection</div>
    </div>
    <div class="service" style="left:88px;top:693px;">
      <div class="service-icon"><svg viewBox="0 0 44 44"><path d="M6 22h16l-2 16H8z"/><path d="M9 22v-3a5 5 0 0 1 10 0v3"/><path d="M32 6v26"/><path d="M26 32h12l2 6H24z"/></svg></div>
      <div>Commercial<br>Cleaning</div>
    </div>
    <div class="service" style="left:418px;top:693px;">
      <div class="service-icon"><svg viewBox="0 0 44 44"><path d="M8 36l10-10 6 6-10 10z"/><path d="M18 26l8-16"/><path d="M28 14h8v14h-8z"/><path d="M30 14v-4h4v4"/></svg></div>
      <div>Construction<br>Cleaning</div>
    </div>

    <div class="brand-name">BrightWay<br>Cleaning</div>

    <div class="contact">
      <p class="contact-name">Dana Whitfield</p>
      <p class="contact-role">Owner/Operator</p>
      <p class="contact-line">Call or Text: (555) 014-2768</p>
      <p class="contact-line">hello@brightwaycleaning.com</p>
    </div>
  </section>
</div>
</body>
</html>
```